Event Graphics for a Summer Camp for Middle School and High School Students

I need graphics designed for our summer camps event. These camps are for teenagers, 6-12th grades. Primary graphic design is for a 11x17 poster but will also need the images resized for:
-social media
-16x9 title slide
- a postcard size
Graphic should include the following:
-Main Title: KL Brightway presents . . . Summer Camp
-Dates: Ignite - June 3-7, High School - June 8-12, Middle School - June 22-26
-Register at KLBrightway.com
-Amberfold Retreat Center, Deadwood, SD
-For each camp, include name and headshot of speaker: Ignite: Mark Tolliver (black jacket photo), High: Danny Ruelas (hispanic man), Middle: Beckett Omari (tan shirt). Gave some options for headshots. Use what works best for cropping.
-Include KL Brightway logo
-Event Graphic should be attractive to teenagers. Open to ideas
My graphic design experience is limited. I will need help receiving the files I need in the various sizes. Thank you.

```html
<!DOCTYPE html>
<html lang="en">
<head>
<meta charset="utf-8">
<title>KL Brightway Summer Camp Poster</title>
<link href="https://fonts.googleapis.com/css2?family=Alfa+Slab+One&family=Andika:wght@400;700&family=Open+Sans:wght@700&family=Sniglet:wght@800&display=swap" rel="stylesheet">
<style>
  :root {
    --sky-deep: #0a84d6;
    --sky-mid: #22c0f0;
    --sky-pale: #e8f8fd;
    --grass-pale: #e2f4a8;
    --grass: #7ccb14;
    --grass-deep: #4aa80a;
    --title-blue: #0a7fd0;
    --ink-blue: #1a3fc4;
    --sun: #fbfd2a;
    --note: #fafb84;
    --pin: #e0222a;
    --page: #ffffff;
  }
  * { box-sizing: border-box; margin: 0; padding: 0; }
  html, body { width: 1200px; height: 1200px; overflow: hidden; background: var(--page); }
  .poster {
    position: absolute; left: 238px; top: 40px; width: 724px; height: 1119px;
    overflow: hidden;
    background: linear-gradient(180deg, var(--sky-deep) 0%, var(--sky-mid) 22%, var(--sky-pale) 40%, #f4fbf0 46%, var(--grass-pale) 60%, var(--grass) 80%, var(--grass-deep) 94%);
  }
  .headline { position: absolute; left: 0; top: 0; width: 724px; height: 440px; }
  .brand { font-family: "Andika", sans-serif; font-weight: 700; font-size: 26px; fill: var(--ink-blue); }
  .presents { font-family: "Andika", sans-serif; font-weight: 700; font-size: 28px; fill: var(--ink-blue); }
  .title { font-family: "Alfa Slab One", serif; fill: var(--title-blue); stroke: var(--sun); stroke-width: 12px; paint-order: stroke; stroke-linejoin: round; }
  .speaker {
    position: absolute; width: 202px; height: 213px; background: var(--note);
    box-shadow: 3px 5px 5px rgba(0,0,0,.3);
  }
  .speaker-photo { position: absolute; left: 13px; top: 14px; width: 176px; height: 147px; }
  .speaker-name {
    position: absolute; left: 0; right: 0; top: 168px; text-align: center;
    font-family: "Sniglet", sans-serif; font-weight: 800; font-size: 22px; color: var(--ink-blue); letter-spacing: -.5px;
  }
  .pin { position: absolute; left: 50%; top: -22px; width: 20px; height: 34px; margin-left: -10px; }
  .speaker--ignite { left: 22px; top: 491px; transform: rotate(-1.5deg); }
  .speaker--middle { left: 260px; top: 487px; transform: rotate(1deg); }
  .speaker--high { left: 492px; top: 481px; transform: rotate(-2deg); }
  .photo--ignite { background: linear-gradient(135deg, #0e2a66, #1d55b0 45%, #101830); }
  .photo--middle { background: linear-gradient(160deg, #2f3a1c, #566232 50%, #c9b49a); }
  .photo--high { background: linear-gradient(160deg, #8a6a4a, #b89c7a 45%, #c9a0a8); }
  .schedule { position: absolute; left: 0; top: 737px; width: 724px; height: 118px; }
  .camp {
    position: absolute; top: 14px; text-align: center; transform: translateX(-50%);
    font-family: "Open Sans", sans-serif; font-weight: 700; font-size: 26px; color: var(--ink-blue);
    letter-spacing: 3px; line-height: 48px; white-space: nowrap;
  }
  .camp--ignite { left: 122px; }
  .camp--middle { left: 354px; }
  .camp--high { left: 598px; }
  .divider { position: absolute; top: 0; width: 5px; height: 118px; background: var(--ink-blue); }
  .register {
    position: absolute; left: 115px; top: 879px; width: 499px; height: 60px; border-radius: 12px;
    background: var(--sun); text-align: center; line-height: 58px;
    font-family: "Andika", sans-serif; font-weight: 700; font-size: 32px; color: var(--ink-blue);
  }
  .venue {
    position: absolute; left: 0; right: 0; top: 950px; text-align: center;
    font-family: "Andika", sans-serif; font-size: 34px; line-height: 46px; color: var(--sun);
  }
  .info-bar {
    position: absolute; left: 0; bottom: 0; width: 724px; height: 64px; background: var(--title-blue);
    text-align: center; line-height: 64px;
    font-family: "Andika", sans-serif; font-weight: 700; font-size: 32px; color: var(--sun);
  }
</style>
</head>
<body>
<main class="poster">
  <svg class="headline" viewBox="0 0 724 440" aria-label="KL Brightway presents Summer Camp">
    <defs>
      <filter id="banner-shadow" x="-10%" y="-10%" width="130%" height="130%">
        <feDropShadow dx="6" dy="8" stdDeviation="4" flood-color="#000" flood-opacity=".45"/>
      </filter>
    </defs>
    <polygon points="112,65 520,126 614,126 614,350 112,387" fill="var(--sun)" filter="url(#banner-shadow)"/>
    <text class="brand" x="126" y="123">KL Brightway</text>
    <text class="presents" x="296" y="123">presents</text>
    <text class="title" x="80" y="246" font-size="138" textLength="598" lengthAdjust="spacingAndGlyphs">SUMMER</text>
    <text class="title" x="160" y="368" font-size="150" textLength="404" lengthAdjust="spacingAndGlyphs">CAMP</text>
  </svg>

  <figure class="speaker speaker--ignite">
    <svg class="pin" viewBox="0 0 20 34"><line x1="10" y1="20" x2="10" y2="33" stroke="#888" stroke-width="2"/><ellipse cx="10" cy="7" rx="6" ry="6" fill="var(--pin)"/><rect x="7" y="10" width="6" height="8" fill="var(--pin)"/><ellipse cx="10" cy="19" rx="9" ry="4" fill="var(--pin)"/></svg>
    <div class="speaker-photo photo--ignite" role="img" aria-label="Photo of speaker Mark Tolliver on stage with a microphone"></div>
    <figcaption class="speaker-name">MARK TOLLIVER</figcaption>
  </figure>
  <figure class="speaker speaker--middle">
    <svg class="pin" viewBox="0 0 20 34"><line x1="10" y1="20" x2="10" y2="33" stroke="#888" stroke-width="2"/><ellipse cx="10" cy="7" rx="6" ry="6" fill="var(--pin)"/><rect x="7" y="10" width="6" height="8" fill="var(--pin)"/><ellipse cx="10" cy="19" rx="9" ry="4" fill="var(--pin)"/></svg>
    <div class="speaker-photo photo--middle" role="img" aria-label="Headshot of speaker Beckett Omari in front of trees"></div>
    <figcaption class="speaker-name">BECKETT OMARI</figcaption>
  </figure>
  <figure class="speaker speaker--high">
    <svg class="pin" viewBox="0 0 20 34"><line x1="10" y1="20" x2="10" y2="33" stroke="#888" stroke-width="2"/><ellipse cx="10" cy="7" rx="6" ry="6" fill="var(--pin)"/><rect x="7" y="10" width="6" height="8" fill="var(--pin)"/><ellipse cx="10" cy="19" rx="9" ry="4" fill="var(--pin)"/></svg>
    <div class="speaker-photo photo--high" role="img" aria-label="Headshot of speaker Danny Ruelas outdoors in the city"></div>
    <figcaption class="speaker-name">DANNY RUELAS</figcaption>
  </figure>

  <section class="schedule">
    <div class="camp camp--ignite">IGNITE<br>JUNE 3-7</div>
    <div class="divider" style="left:217px"></div>
    <div class="camp camp--middle">MIDDLE SCHOOL<br>JUNE 22-26</div>
    <div class="divider" style="left:481px"></div>
    <div class="camp camp--high">HIGH SCHOOL<br>JUNE 8-12</div>
  </section>

  <p class="register">Register at: KLBrightway.com</p>
  <p class="venue">Amberfold Retreat Center,<br>Deadwood, SD</p>
  <footer class="info-bar">For more info. call us : 000-000-0000</footer>
</main>
</body>
</html>
```